Company Profile
Corvane Logistics Sdn Bhd is a well established and experienced freight forwarder in Kuala Lumpur, Malaysia. We specialize in air and sea forwarding, Custom Brokerage and regulatory compliance services, inland transportation,
overseas freighting and warehousing and distribution management. With our dedicated qualified and experienced professionals, we are fully committed to serving our clients.

Our Mission
Based on the motto “Quick, Reliable and Polite”, Corvane Logistics is dedicated to upholding the following three points corporate philosophy:
1. Adhering to the principle that “the customer always comes first”.
2. Contributing to the development of the local community.
3. Making it our duty to be responsible and sincere.

Our Edge
• One-Stop Logistics Solutions
• Extensive Network Throughout Malaysia
• Highly Qualified and Experienced Pool of Professionals
• Comprehensive IT Solutions
• Innovative and Customer-focused Solutions
• Flexible and Consistent in Managing Exceptions
• Total Supply Chain Visibility

Target Market(s)

We sell the logistics services to all the industry in Malaysia. (ONE Stop Logistics Solutions)

Industry/Entity Type

Logistic

Contact Information for Business Card

I want the back of the card to be white with the logo and slogan. i would like to see the logo on the front with the general info.

Requirements
Must have
• Name, Title, Office, Cell, Fax, Email, Address, Website
Nice to have
• Modern Design Business Card

```html
<!DOCTYPE html>
<html lang="en">
<head>
<meta charset="utf-8">
<title>Corvane Logistics — Stationery Set</title>
<link href="https://fonts.googleapis.com/css2?family=Open+Sans:wght@400;600;700&display=swap" rel="stylesheet">
<style>
  :root {
    --brand-blue: #2f8dc3;
    --band-grey: #6f7072;
    --ink: #4a4a4c;
    --ink-soft: #7a7b7d;
    --paper: #f7f7f7;
    --backdrop: #ebecec;
    --white: #ffffff;
  }
  * { box-sizing: border-box; margin: 0; padding: 0; }
  html, body { width: 1200px; height: 925px; overflow: hidden; }
  body {
    background: var(--backdrop);
    font-family: "Open Sans", Arial, sans-serif;
    color: var(--ink);
    position: relative;
  }
  address { font-style: normal; }
  .sheet { position: absolute; background: var(--paper); overflow: hidden; }

  .wordmark { font-weight: 600; color: var(--brand-blue); line-height: 1.05; display: flex; align-items: center; gap: 5px; }
  .wordmark .dot { width: 7px; height: 7px; border-radius: 50%; background: var(--brand-blue); flex: none; }
  .wordmark.on-blue { color: var(--white); }
  .wordmark.on-blue .dot { background: var(--white); }

  /* Letterhead */
  .letterhead { left: 230px; top: 114px; width: 340px; height: 484px; }
  .letterhead .wordmark { position: absolute; left: 20px; top: 52px; font-size: 10px; }
  .letterhead .address { position: absolute; right: 17px; top: 34px; text-align: right; font-size: 5.2px; line-height: 1.6; color: var(--ink); }
  .letterhead .address strong { font-weight: 700; }
  .footer-band { position: absolute; left: 0; bottom: 0; width: 100%; }
  .footer-text { position: absolute; left: 0; width: 100%; text-align: center; color: var(--white); font-size: 5.4px; white-space: nowrap; }

  /* Folder */
  .folder { left: 630px; top: 94px; width: 402px; height: 506px; background: var(--brand-blue); }
  .folder .spine { position: absolute; left: 0; top: 0; width: 24px; height: 100%; background: var(--band-grey); }
  .folder .wordmark { position: absolute; left: 24px; right: 0; top: 0; bottom: 0; justify-content: center; font-size: 30px; gap: 12px; }
  .folder .wordmark .dot { width: 18px; height: 18px; }

  /* Business card front */
  .card-front { left: 107px; top: 640px; width: 154px; height: 88px; }
  .card-front .wordmark { position: absolute; left: 9px; top: 34px; width: 58px; font-size: 7px; gap: 3px; }
  .card-front .wordmark .dot { width: 5px; height: 5px; }
  .card-front .person { position: absolute; left: 72px; right: 5px; top: 8px; }
  .card-front .person-name { font-size: 6.5px; font-weight: 700; color: var(--brand-blue); }
  .card-front .person-title { font-size: 4.2px; color: var(--ink-soft); margin-bottom: 4px; }
  .card-front .details { font-size: 3.5px; line-height: 1.55; color: var(--ink); white-space: nowrap; }
  .card-front .details strong { font-weight: 700; }
  .card-front .row { display: flex; align-items: center; gap: 2px; }
  .card-front .row svg { width: 4px; height: 4px; flex: none; }

  /* Business card back */
  .card-back { left: 107px; top: 752px; width: 155px; height: 88px; background: var(--brand-blue); color: var(--white); text-align: center; }
  .card-back .wordmark { justify-content: center; font-size: 8px; margin-top: 16px; gap: 3px; }
  .card-back .wordmark .dot { width: 5px; height: 5px; }
  .card-back .spec-title { display: flex; align-items: center; gap: 4px; margin: 14px 10px 2px; font-size: 4.6px; }
  .card-back .spec-title::before, .card-back .spec-title::after { content: ""; flex: 1; height: 0.5px; background: var(--white); }
  .card-back .services { font-size: 3.3px; line-height: 1.5; padding: 0 8px; }
  .card-back .slogan { font-size: 3.8px; font-weight: 700; margin-top: 1px; }

  /* Compliment card */
  .compliment { left: 301px; top: 652px; width: 381px; height: 184px; }
  .compliment .wordmark { position: absolute; left: 18px; top: 58px; font-size: 11px; }
  .compliment .footer-text { font-size: 5.8px; }

  /* Envelope */
  .envelope { left: 720px; top: 652px; width: 382px; height: 184px; }
  .envelope .flap { position: absolute; left: 0; top: 0; width: 100%; height: 66px; }
  .envelope .wordmark { position: absolute; left: 0; right: 0; top: 16px; justify-content: center; font-size: 8.5px; gap: 4px; }
  .envelope .wordmark .dot { width: 5px; height: 5px; }
  .envelope .web { position: absolute; left: 0; right: 0; top: 43px; text-align: center; color: var(--white); font-size: 5.6px; font-style: italic; }
</style>
</head>
<body>

  <!-- Letterhead -->
  <section class="sheet letterhead" aria-label="Letterhead">
    <div class="wordmark"><span class="dot"></span>Corvane Logistics</div>
    <address class="address">
      <strong>CORVANE LOGISTICS SDN. BHD. (1284630-K)</strong><br>
      No. 8B, 2nd Floor, Jalan Seri Mutiara 3<br>
      Taman Mutiara, 41050 Klang<br>
      Selangor Darul Ehsan, Malaysia.
    </address>
    <svg class="footer-band" width="340" height="36" viewBox="0 0 340 36" aria-hidden="true">
      <path d="M0 36 L0 20 Q170 -8 340 20 L340 36 Z" fill="var(--band-grey)"/>
      <path d="M0 36 L0 23 Q170 -4 340 23 L340 36 Z" fill="var(--brand-blue)"/>
    </svg>
    <p class="footer-text" style="bottom:16px;">P : (603) 5521 0480 / 0481 &nbsp; C : +6012-470 2815</p>
    <p class="footer-text" style="bottom:5px;">F : (603) 5521 0490 &nbsp; E : farid@corvane.com.my &nbsp; W : www.corvane.com.my</p>
  </section>

  <!-- Presentation folder -->
  <section class="sheet folder" aria-label="Presentation folder">
    <div class="spine"></div>
    <div class="wordmark on-blue"><span class="dot"></span>Corvane Logistics</div>
  </section>

  <!-- Business card, front -->
  <section class="sheet card-front" aria-label="Business card front">
    <div class="wordmark"><span class="dot"></span><span>Corvane<br>Logistics</span></div>
    <div class="person">
      <p class="person-name">Farid Hamzah</p>
      <p class="person-title">Managing Director</p>
      <address class="details">
        <strong>CORVANE LOGISTICS SDN. BHD. (1284630-K)</strong><br>
        No. 8B, 2nd Floor, Jalan Seri Mutiara 3<br>
        Taman Mutiara, 41050 Klang<br>
        Selangor Darul Ehsan, Malaysia.
        <div class="row"><svg viewBox="0 0 10 10"><path d="M2 1 L4 1 L5 3 L4 4 Q5 6 6 6 L7 5 L9 6 L9 8 Q5 9 2 5 Q1 3 2 1Z" fill="var(--brand-blue)"/></svg>(603) 5521 0480 / 0481</div>
        <div class="row"><svg viewBox="0 0 10 10"><rect x="3" y="1" width="4" height="8" rx="1" fill="var(--brand-blue)"/></svg>+6012-470 2815</div>
        <div class="row"><svg viewBox="0 0 10 10"><rect x="1" y="4" width="8" height="5" fill="var(--brand-blue)"/><rect x="3" y="1" width="4" height="3" fill="var(--brand-blue)"/></svg>(603) 5521 0490</div>
        <div class="row"><svg viewBox="0 0 10 10"><rect x="1" y="2" width="8" height="6" fill="var(--brand-blue)"/></svg>farid@corvane.com.my</div>
        <div class="row"><svg viewBox="0 0 10 10"><circle cx="5" cy="5" r="4" fill="var(--brand-blue)"/></svg>www.corvane.com.my</div>
      </address>
    </div>
  </section>

  <!-- Business card, back -->
  <section class="sheet card-back" aria-label="Business card back">
    <div class="wordmark on-blue"><span class="dot"></span>Corvane Logistics</div>
    <p class="spec-title">We're Specialize In</p>
    <p class="services">
      International Shipping Air | Sea | Customs Brokerage | Project Cargo<br>
      Supply Chain Management | Tax Consultancy | Warehousing<br>
      Transportation | Haulage | Packing | Marine Insurance<br>
      Distribution | Door to Door
    </p>
    <p class="slogan">ONE STOP LOGISTICS SOLUTIONS</p>
  </section>

  <!-- Compliment card -->
  <section class="sheet compliment" aria-label="Compliment card">
    <div class="wordmark"><span class="dot"></span>Corvane Logistics</div>
    <svg class="footer-band" width="381" height="36" viewBox="0 0 381 36" aria-hidden="true">
      <path d="M0 36 L0 20 Q190 -8 381 20 L381 36 Z" fill="var(--band-grey)"/>
      <path d="M0 36 L0 23 Q190 -4 381 23 L381 36 Z" fill="var(--brand-blue)"/>
    </svg>
    <p class="footer-text" style="bottom:15px;"><strong>CORVANE LOGISTICS SDN. BHD. (1284630-K)</strong>, No. 8B, 2nd Floor, Jalan Seri Mutiara 3</p>
    <p class="footer-text" style="bottom:5px;">Taman Mutiara, 41050 Klang, Selangor Darul Ehsan, Malaysia.</p>
  </section>

  <!-- Envelope -->
  <section class="sheet envelope" aria-label="Envelope">
    <svg class="flap" width="382" height="66" viewBox="0 0 382 66" aria-hidden="true">
      <path d="M0 0 L382 0 L382 40 Q378 62 356 62 L26 62 Q4 62 0 40 Z" fill="var(--brand-blue)"/>
    </svg>
    <div class="wordmark on-blue"><span class="dot"></span>Corvane Logistics</div>
    <p class="web">www.corvane.com.my</p>
  </section>

</body>
</html>
```